Brandomir tile letterhead contractor

I would like to get a very good expressive letterhead or resume with great 3D design as a tile contractor company offering my services to others tile companies, general contractors and home owners clients. (This is the idea)
Founder/owner.
“Proud to represent and provide my life’s passion services as brandomir tile.”
I’m journeyman setter, I have passion for creating visually stunning designs with a focus on creativity usability. I have been working as setter with a remarkable companies for over 20 years and I specialize in commercial and residential projects.
My experience and expertise have enabled me to create beautiful master pieces for a wide range of clients, from a small businesses to a large corporations.
My first goal in any project that you hire me for is to provide a professional and high-quality product that meets and exceeds your expectations. You can really assured that I will strive tirelessly to produce the best results for our clients until the final project is done.
*My team will move forward with your needs in every step we walk together
*We have a very solid foundations knowledge altogether rely in the best equipment possible to make (builds)what it takes with best quality possible
*I’m an independent contractor and beaten to another prestigious companies …. ETC. ETC.
ILL TRY TO KEEP UPDATING MORE INFO.
Target Market(s)
General contractors, tile companies and home owners builders
Industry/Entity Type
Tile construction
Look and feel

```html
<!DOCTYPE html>
<html lang="en">
<head>
<meta charset="utf-8">
<title>Brandomir Tile Letterhead</title>
<link rel="stylesheet" href="https://fonts.googleapis.com/css2?family=Open+Sans:wght@400;600&family=Arimo:wght@400;700&display=swap">
<style>
  :root {
    --backdrop: #e2e2e2;
    --paper: #ffffff;
    --brand: #5b4340;
    --ink: #555555;
    --ink-dark: #3f3f3f;
    --sign-fill: #e9e6e5;
  }
  * { margin: 0; padding: 0; box-sizing: border-box; }
  html, body { width: 1200px; height: 1200px; overflow: hidden; background: var(--backdrop); }
  .letterhead {
    position: absolute; left: 240px; top: 90px;
    width: 720px; height: 1019px; background: var(--paper);
  }
  .brand-name {
    position: absolute; left: 50px; top: 107px; width: 202px;
    display: flex; align-items: center; justify-content: center; gap: 7px;
    font: 600 17px/1 "Open Sans", sans-serif; letter-spacing: 1.6px;
    color: var(--brand); white-space: nowrap;
  }
  .brand-mark { width: 9px; height: 9px; background: var(--brand); flex: none; }
  .rule-thick { position: absolute; top: 131px; height: 4px; background: var(--brand); }
  .rule-thick.left { left: 0; width: 70px; }
  .rule-thick.right { left: 234px; right: 0; }
  .rule-thin { position: absolute; left: 0; right: 0; top: 143px; height: 1.5px; background: var(--brand); }
  .tagline {
    position: absolute; left: 70px; width: 164px; top: 130px; text-align: center;
    font: 400 6.5px/1 "Open Sans", sans-serif; letter-spacing: 1.9px; color: var(--brand);
    white-space: nowrap;
  }
  .contact {
    position: absolute; font: 400 13px/1 "Open Sans", sans-serif; color: var(--brand);
    display: flex; align-items: center; gap: 6px; white-space: nowrap;
  }
  .contact svg { width: 11px; height: 11px; fill: var(--brand); flex: none; }
  .contact.left { left: 278px; }
  .contact.right { right: 56px; }
  .contact .square { width: 10px; height: 10px; background: var(--brand); flex: none; }
  .salutation {
    position: absolute; left: 66px; top: 316px;
    font: 700 15px/1 Arimo, sans-serif; color: var(--ink-dark);
  }
  .body-copy { position: absolute; left: 64px; top: 360px; width: 592px; }
  .body-copy p {
    font: 400 12.5px/14.6px Arimo, sans-serif; color: var(--ink);
    margin-bottom: 13px;
  }
  .closing {
    position: absolute; left: 65px; top: 668px;
    font: 700 8.5px/1 Arimo, sans-serif; color: var(--ink-dark);
  }
  .signature {
    position: absolute; left: 64px; top: 710px; width: 118px; height: 34px;
    background: var(--sign-fill); border-radius: 3px;
  }
</style>
</head>
<body>
<main class="letterhead">
  <header>
    <div class="brand-name"><span class="brand-mark"></span>BRANDOMIR TILE</div>
    <div class="rule-thick left"></div>
    <div class="tagline">CRAFTED TILE, SET TO LAST</div>
    <div class="rule-thick right"></div>
    <div class="rule-thin"></div>

    <div class="contact left" style="top:86px">
      <svg viewBox="0 0 24 24" aria-hidden="true"><path d="M6.6 10.8a15.1 15.1 0 0 0 6.6 6.6l2.2-2.2c.3-.3.7-.4 1-.2 1.1.4 2.3.6 3.6.6.6 0 1 .4 1 1V20c0 .6-.4 1-1 1C10.6 21 3 13.4 3 4c0-.6.4-1 1-1h3.5c.6 0 1 .4 1 1 0 1.3.2 2.5.6 3.6.1.3 0 .7-.2 1L6.6 10.8z"/></svg>
      (555) 014-2290
    </div>
    <div class="contact left" style="top:106px">
      <svg viewBox="0 0 24 24" aria-hidden="true"><path d="M2 6.5V19h20V6.5l-10 7.5z M2.5 5h19L12 12.2z"/></svg>
      hello@brandomirtile.com
    </div>
    <div class="contact right" style="top:84px">
      www.social.example/Brandomirtile <span class="square"></span>
    </div>
    <div class="contact right" style="top:103px">
      Eastbrook Utah, 84000
      <svg viewBox="0 0 24 24" aria-hidden="true"><path d="M12 2a7 7 0 0 0-7 7c0 5 7 13 7 13s7-8 7-13a7 7 0 0 0-7-7zm0 9.5A2.5 2.5 0 1 1 12 6.5a2.5 2.5 0 0 1 0 5z"/></svg>
    </div>
  </header>

  <section class="letter">
    <h1 class="salutation">Dear Mr. Harlow,</h1>
    <div class="body-copy">
      <p>Lorem ipsum dolor sit amet, consectetuer adipiscing elit, sed diam nonmmy nibh euismod tincidunt ut laor eet dolore magna aliquam erat volutpat. Ut wisi enim ad minim veniam, quis nostrud exerci tationmcorper suscipit lobortis nisl ut aliquip ex ea commodo consequat. Duis autem vel eum iriure dolor in hendrerit in vulputate velit esse molestie consequat, vel illum dolore eu feugiat</p>
      <p>Rorem ipsum dolor sit amet, consectetuer adipiscing elit, sed diam nonmmy nibh euismod tincidunt ut laor eet dolore magna aliquam erat volutpat. Ut wisi enim ad minim veniam, quis nostrud exerci tationmcorper suscipit lobortis nisl ut aliquip ex ea commodo consequat. Duis autem vel eum iriure dolor in hendrerit in vulputate velit esse molest</p>
      <p>Dorem ipsum dolor sit amet, consectetuer adipiscing elit, sed diam nonmmy nibh euismod tincidunt ut laor eet dolore magna aliquam erat volutpat. Ut wisi enim ad minim veniam, quis nostrud exerci tationmcorper suscipit lobortis nisl ut aliquip ex ea commodo consequat. Duis autem vel eum iriure dolor in hendrerit in suscipit lobortis nisl ut aliquip ex ea commodo consequat. Duis autem vel eum iriure dolor in hendrerit in vulputate velit esse molestie consequat, vel illum</p>
      <p>Sorem ipsum dolor sit amet, consectetuer adipiscing elit, sed diam nonmmy nibh euismod tincidunt ut laor eet dolore magna aliquam erat volutpat. Ut wisi enim ad minim veniam, quis nostrud exerci tationmcorper suscipit lobortis nisl ut aliquip ex ea commodo consequat. Duis autem vel eum iriure dolor in</p>
    </div>
    <p class="closing">Sincerely,</p>
    <div class="signature" role="img" aria-label="Handwritten signature of the owner"></div>
  </section>
</main>
</body>
</html>
```